Stationary/business card design for Harborline Building Partners
Harborline Building Partners
Stationary/business card design for Harborline Building Partners - Consulting
Creative Brief
Use specific fonts
Up to designer. Can be different from logo if that looks good.
Simple
Clara T Revanski
Director - Business Development & Support
3870 Wexmoor Avenue - Suite 2C Rochester, NY 14618
clara.revanski@hbpworkline.com
www.HBPworkline.com
The back of the business card will have some of what we do on there, for example: GIS, Drafting, Master Data. I haven't written that up yet.

```html
<!DOCTYPE html>
<html lang="en">
<head>
<meta charset="utf-8">
<title>Harborline Building Partners – Stationery</title>
<link href="https://fonts.googleapis.com/css2?family=Cinzel:wght@600&family=Open+Sans:wght@400;600&display=swap" rel="stylesheet">
<style>
:root{
  --green:#1fb43a;
  --ink:#111;
  --paper:#fff;
  --grey:#6d6d6d;
  --ground:#e9e9e7;
  --faint:#e3ece5;
}
*{box-sizing:border-box;margin:0;padding:0}
html,body{width:1200px;height:466px;overflow:hidden}
body{background:var(--ground);font-family:"Open Sans",Arial,sans-serif;color:var(--ink);position:relative}
.piece{position:absolute;background:var(--paper);box-shadow:0 2px 6px rgba(0,0,0,.18);overflow:hidden}
.label{position:absolute;font-size:5px;letter-spacing:.5px;text-transform:uppercase;color:#8a8a8a;text-align:center}
.brand{font-family:"Cinzel",Georgia,serif;font-weight:600;color:var(--green);display:flex;align-items:center;gap:4px;line-height:1.05;text-transform:uppercase}
.brand .dot{width:8px;height:8px;border-radius:50%;background:var(--green);flex:none}
.swoosh{position:absolute;left:0;bottom:0;width:100%;display:block}
.contact{font-size:4px;line-height:1.45;color:var(--grey);white-space:nowrap}

.card-front{left:12px;top:216px;width:96px;height:56px}
.card-front .brand{position:absolute;left:6px;top:8px;font-size:5px}
.card-front .contact{position:absolute;left:6px;top:24px;font-size:3px}
.card-back{left:12px;top:300px;width:96px;height:56px;background:var(--green)}
.card-back .brand{color:var(--paper);font-size:6px;position:absolute;left:50%;top:50%;transform:translate(-50%,-50%);white-space:nowrap}
.card-back .brand .dot{background:var(--paper)}

.letter{top:29px;width:360px;height:418px}
.letter-one{left:132px}
.letter-two{left:522px}
.letter .brand{position:absolute;left:18px;top:18px;font-size:8px;width:110px}
.letter .contact{position:absolute;left:128px;top:16px}
.watermark{position:absolute;left:0;right:0;top:150px;text-align:center;font-family:"Cinzel",Georgia,serif;font-weight:600;font-size:40px;line-height:1.05;color:var(--faint);text-transform:uppercase}

.env-open{left:912px;top:22px;width:264px;height:150px;background:none;box-shadow:none}
.env-back{left:912px;top:190px;width:264px;height:118px}
.env-back .brand{position:absolute;left:50%;top:44px;transform:translateX(-50%);font-size:8px;white-space:nowrap}
.env-front{left:912px;top:328px;width:264px;height:118px}
.env-front .brand{position:absolute;left:16px;top:14px;font-size:6px}
.env-front .contact{position:absolute;left:110px;top:64px;font-size:3.4px}
</style>
</head>
<body>
<p class="label" style="left:12px;top:200px;width:96px">Stationery Concepts</p>

<section class="piece card-front">
  <div class="brand"><span class="dot"></span><span>Harborline<br>Building Partners</span></div>
  <div class="contact">Clara T Revanski<br>Director - Business Development &amp; Support<br>3870 Wexmoor Avenue - Suite 2C Rochester, NY 14618<br>clara.revanski@hbpworkline.com<br>www.HBPworkline.com</div>
  <svg class="swoosh" viewBox="0 0 96 18" preserveAspectRatio="none"><path d="M0 18V11C30 17 62 13 96 0V18Z" fill="var(--green)"/></svg>
</section>
<p class="label" style="left:12px;top:280px;width:96px">Business Card Front</p>

<section class="piece card-back">
  <div class="brand"><span class="dot"></span><span>Harborline</span></div>
</section>
<p class="label" style="left:12px;top:364px;width:96px">Business Card Back</p>

<section class="piece letter letter-one">
  <div class="brand"><span class="dot"></span><span>Harborline<br>Building Partners</span></div>
  <div class="contact">Clara T Revanski<br>3870 Wexmoor Avenue - Suite 2C<br>Rochester, NY 14618<br>Phone 585 555 0142<br>Fax 585 555 0143<br>Mobile 585 555 0144<br>clara.revanski@hbpworkline.com<br>www.HBPworkline.com</div>
  <svg class="swoosh" viewBox="0 0 360 120" preserveAspectRatio="none">
    <path d="M0 120V68C120 118 250 80 360 6V120Z" fill="var(--green)"/>
    <path d="M0 60C120 110 250 72 360 0" fill="none" stroke="var(--ink)" stroke-width="2"/>
  </svg>
</section>
<p class="label" style="left:132px;top:452px;width:360px">Letter Head Option 1</p>

<section class="piece letter letter-two">
  <div class="brand"><span class="dot"></span><span>Harborline<br>Building Partners</span></div>
  <div class="contact">Clara T Revanski<br>3870 Wexmoor Avenue - Suite 2C<br>Rochester, NY 14618<br>Phone 585 555 0142<br>Fax 585 555 0143<br>Mobile 585 555 0144<br>clara.revanski@hbpworkline.com<br>www.HBPworkline.com</div>
  <div class="watermark" aria-hidden="true">Harborline<br>Building Partners</div>
  <svg class="swoosh" viewBox="0 0 360 120" preserveAspectRatio="none">
    <path d="M0 120V68C120 118 250 80 360 6V120Z" fill="var(--green)"/>
    <path d="M0 60C120 110 250 72 360 0" fill="none" stroke="var(--ink)" stroke-width="2"/>
  </svg>
</section>
<p class="label" style="left:522px;top:452px;width:360px">Letter Head Option 2</p>

<section class="piece env-open" aria-label="Envelope back, flap open">
  <svg width="264" height="150" viewBox="0 0 264 150">
    <path d="M4 0H260Q264 0 264 4V70C190 40 74 40 0 70V4Q0 0 4 0Z" fill="var(--green)"/>
    <rect x="0" y="62" width="264" height="88" fill="var(--ink)"/>
    <path d="M0 150V100C80 84 184 84 264 100V150Z" fill="var(--paper)"/>
    <path d="M0 100C80 84 184 84 264 100" fill="none" stroke="var(--green)" stroke-width="3"/>
  </svg>
</section>

<section class="piece env-back">
  <svg class="swoosh" style="top:0;bottom:auto" viewBox="0 0 264 30" preserveAspectRatio="none"><path d="M0 0H264V8C180 30 84 30 0 8Z" fill="var(--green)"/></svg>
  <div class="brand"><span class="dot"></span><span>Harborline</span></div>
</section>

<section class="piece env-front">
  <div class="brand"><span class="dot"></span><span>Harborline<br>Building Partners</span></div>
  <div class="contact">3870 Wexmoor Avenue - Suite 2C Rochester, NY 14618</div>
  <svg class="swoosh" viewBox="0 0 264 40" preserveAspectRatio="none">
    <path d="M0 40V26C90 40 180 30 264 4V40Z" fill="var(--green)"/>
    <path d="M0 22C90 36 180 26 264 0" fill="none" stroke="var(--ink)" stroke-width="1.5"/>
  </svg>
</section>
<p class="label" style="left:912px;top:450px;width:264px">Envelope Option 1</p>
</body>
</html>
```